" Trabalhamos visitando nossos clientes no porta a portas, clientes esses com escolas, colégios e creches particulares e prefeituras. Fora a venda particular, participamos de licitações em prefeituras. "

```html
<!DOCTYPE html>
<html lang="pt-BR">
<head>
<meta charset="UTF-8">
<title>Nova Linha Comercial — Papel Timbrado</title>
<link href="https://fonts.googleapis.com/css2?family=Montserrat:wght@500;700&display=swap" rel="stylesheet">
<style>
  :root {
    --canvas: #f1f1f1;
    --paper: #ffffff;
    --gold: #d1bb6b;
    --gold-deep: #b8962f;
    --ink: #3a3a3a;
    --ink-soft: #555555;
  }
  html, body {
    margin: 0;
    padding: 0;
    width: 1200px;
    height: 1200px;
    overflow: hidden;
    background: var(--canvas);
    font-family: "Montserrat", sans-serif;
  }
  .letterhead {
    position: absolute;
    left: 329px;
    top: 132px;
    width: 547px;
    height: 888px;
    background: var(--paper);
  }
  .side-band {
    position: absolute;
    left: 0;
    top: 0;
    width: 36px;
    height: 100%;
    background: var(--gold);
  }
  .brand {
    position: absolute;
    left: 55px;
    top: 48px;
    display: flex;
    align-items: center;
    gap: 10px;
  }
  .brand-mark {
    width: 22px;
    height: 22px;
    background: var(--gold-deep);
  }
  .brand-name {
    font-weight: 500;
    font-size: 15px;
    letter-spacing: 1.5px;
    color: var(--ink);
    text-transform: uppercase;
  }
  .contact-bar {
    position: absolute;
    left: 55px;
    right: 24px;
    top: 814px;
    display: flex;
    align-items: center;
    gap: 18px;
  }
  .contact-item {
    display: flex;
    align-items: center;
    gap: 6px;
    font-weight: 700;
    font-size: 7.5px;
    letter-spacing: 0.3px;
    color: var(--ink-soft);
    text-transform: uppercase;
    white-space: nowrap;
  }
  .contact-icon {
    width: 16px;
    height: 16px;
    display: block;
  }
</style>
</head>
<body>
  <main class="letterhead">
    <div class="side-band"></div>

    <header class="brand">
      <span class="brand-mark"></span>
      <span class="brand-name">Nova Linha Comercial</span>
    </header>

    <footer class="contact-bar">
      <div class="contact-item">
        <svg class="contact-icon" viewBox="0 0 16 16" aria-hidden="true">
          <rect width="16" height="16" rx="3" fill="#c9a646"/>
          <path d="M5 4l2 2-1 1c.6 1.3 1.7 2.4 3 3l1-1 2 2-1.2 1.2C7.5 12 4 8.5 3.8 5.2z" fill="#fff"/>
        </svg>
        <span>(83) 90000-1234 | 90000-5678</span>
      </div>
      <div class="contact-item">
        <svg class="contact-icon" viewBox="0 0 16 16" aria-hidden="true">
          <rect width="16" height="16" rx="3" fill="#c9a646"/>
          <rect x="3.5" y="5" width="9" height="6.5" fill="none" stroke="#fff" stroke-width="1.2"/>
          <path d="M3.5 5l4.5 3.6L12.5 5" fill="none" stroke="#fff" stroke-width="1.2"/>
        </svg>
        <span>novalinha@mail.com</span>
      </div>
      <div class="contact-item">
        <svg class="contact-icon" viewBox="0 0 16 16" aria-hidden="true">
          <rect width="16" height="16" rx="3" fill="#c9a646"/>
          <circle cx="8" cy="8" r="4.5" fill="none" stroke="#fff" stroke-width="1.1"/>
          <ellipse cx="8" cy="8" rx="2" ry="4.5" fill="none" stroke="#fff" stroke-width="1"/>
          <path d="M3.5 8h9" stroke="#fff" stroke-width="1"/>
        </svg>
        <span>novalinha.com.br</span>
      </div>
    </footer>
  </main>
</body>
</html>
```